Yard Sign Design for Roofing Contractor

We are looking for a new design for our yard signs used on all jobs we build. We are looking for a way to brand the company and are hoping that this contest can give us a "theme" we can incorporate into out other marketing items such as, vehicle graphics, apparel, etc... I have attached a copy of our logo to be used on the sign, it can be "shadowed" with a color to enhance the look and the sign, but please keep the basic logo design. Attached are some samples of construction colors the boss was thinking of along with a picture of our current yard sign to help give some direction and let you know what info is needed on the sign.The darker construction yellow may work better than the fluorescent yellow, but won't know without visual aid. We are not tied to any particular color as of now, so they do have freedom of design as long as keeping with the construction feel. (Just another thought, potentially a reflective construction tape look would be interesting so signs are visable at night)
Updates

Reason: Meeting with new web designers next week to discuss best option to incorporate into our website.Thank you for the submissions!

Target Market(s)

Want signs to stand out when driving by and visibility in neighborhood where sign is posted for potential referrals

Industry/Entity Type

Contractor

Colors
fbed22
fece3e
f37122

Requirements
Must have
• Information that is on our current signs, image attached. I uploaded a .pdf file showing some options that could work for adding "shading" to our logo if you choose to do so.
• Sign should measure 18" T, 24" W
Nice to have
• Interested is seeing designs using construction tape look, images attached

```html
<!DOCTYPE html>
<html lang="en">
<head>
<meta charset="utf-8">
<title>Halden Construction Yard Sign</title>
<link rel="stylesheet" href="https://fonts.googleapis.com/css2?family=Cinzel:wght@700&family=Oswald:wght@500&family=Lato:wght@400&display=swap">
<style>
  :root {
    --backdrop: #3a3a3a;
    --sign-yellow: #f7d33c;
    --sign-yellow-deep: #e9b825;
    --stripe-gold: #e6b21c;
    --ink: #0b0b0b;
  }
  html, body {
    margin: 0;
    width: 1200px;
    height: 1200px;
    overflow: hidden;
    background: var(--backdrop);
  }
  .yard-sign {
    position: absolute;
    left: 50px;
    top: 187px;
    width: 1100px;
    height: 825px;
    overflow: hidden;
    background:
      radial-gradient(ellipse at 60% 40%, rgba(255,230,110,0.55) 0%, rgba(255,230,110,0) 60%),
      radial-gradient(ellipse at 15% 80%, rgba(214,160,20,0.35) 0%, rgba(214,160,20,0) 55%),
      var(--sign-yellow);
    box-shadow: 0 6px 18px rgba(0,0,0,0.45);
  }
  .hazard-band {
    position: absolute;
    left: 0;
    width: 100%;
  }
  .hazard-band--top {
    top: 0;
    height: 86px;
    background: repeating-linear-gradient(45deg,
      var(--ink) 0 30px, var(--stripe-gold) 30px 55px);
  }
  .hazard-band--bottom {
    bottom: 0;
    height: 87px;
    background: repeating-linear-gradient(-45deg,
      var(--ink) 0 30px, var(--stripe-gold) 30px 55px);
  }
  .company-url {
    position: absolute;
    top: 238px;
    left: 0;
    width: 100%;
    text-align: center;
    font-family: 'Lato', sans-serif;
    font-size: 29px;
    color: var(--ink);
    margin: 0;
  }
  .company-name {
    position: absolute;
    top: 300px;
    left: 0;
    width: 100%;
    margin: 0;
    text-align: center;
    font-family: 'Cinzel', serif;
    font-weight: 700;
    color: var(--ink);
    line-height: 1;
  }
  .company-name__main {
    display: block;
    font-size: 140px;
    letter-spacing: -3px;
  }
  .company-name__sub {
    display: block;
    margin-top: 8px;
    font-size: 64px;
    letter-spacing: -1px;
  }
  .services {
    position: absolute;
    top: 548px;
    left: 0;
    width: 100%;
    margin: 0;
    text-align: center;
    font-family: 'Cinzel', serif;
    font-weight: 700;
    font-size: 38px;
    color: var(--ink);
    word-spacing: 4px;
  }
  .services__dot {
    display: inline-block;
    margin: 0 30px;
  }
  .phone-line {
    position: absolute;
    top: 608px;
    left: 0;
    width: 100%;
    display: flex;
    justify-content: center;
    align-items: center;
    gap: 26px;
  }
  .phone-line__icon {
    width: 74px;
    height: 74px;
    margin-top: 16px;
  }
  .phone-line__number {
    font-family: 'Oswald', sans-serif;
    font-weight: 500;
    font-size: 112px;
    line-height: 1;
    color: var(--ink);
    letter-spacing: 1px;
  }
</style>
</head>
<body>
  <main class="yard-sign">
    <div class="hazard-band hazard-band--top"></div>

    <p class="company-url">http://www.haldenroofing.com</p>

    <h1 class="company-name">
      <span class="company-name__main">HALDEN</span>
      <span class="company-name__sub">CONSTRUCTION</span>
    </h1>

    <p class="services">ROOF<span class="services__dot">•</span>SIDING<span class="services__dot">•</span>GUTTERS</p>

    <div class="phone-line">
      <svg class="phone-line__icon" viewBox="0 0 74 74" aria-hidden="true">
        <path d="M14 8c4-3 8-3 10 1l6 12c1 3 0 5-2 7l-5 4c3 8 10 16 18 20l5-5c2-2 4-2 7-1l11 6c4 2 4 6 1 10l-5 5c-4 4-11 4-19 0C26 61 12 47 7 32 4 23 5 16 9 12z" fill="var(--ink)"/>
        <path d="M40 26a10 10 0 0 1 9 9" stroke="var(--ink)" stroke-width="4" fill="none" stroke-linecap="round"/>
        <path d="M42 15a21 21 0 0 1 18 18" stroke="var(--ink)" stroke-width="4" fill="none" stroke-linecap="round"/>
        <path d="M44 4a32 32 0 0 1 27 27" stroke="var(--ink)" stroke-width="4" fill="none" stroke-linecap="round"/>
      </svg>
      <span class="phone-line__number">1-405-555-0142</span>
    </div>

    <div class="hazard-band hazard-band--bottom"></div>
  </main>
</body>
</html>
```